Postcard design to acquire new clients for my Property Management Company

I'm looking for a postcard design that I can send to prospective clients detailing information about my company and services.
Postcard should be eye catching and contain information from www.brightkeyrentals-example.com. I've provided a few screen shots for the most important information and my logo.
Target Market(s)
Real Estate
Industry/Entity Type
Real Estate
Font styles to use
Sans Serif
Requirements
Must have
- Must be eye catching!! this will be a direct mail piece - I'd like for the card to be read and not tossed in the trash immediately.
Design que from the logo.
A place to write / print the receipts name and address.
our physical address - 2287 Marble Lane, Lubbock, TX 79555.
Should not have
- the contact information on the business card is not accurate - please use info from website.

```html
<!DOCTYPE html>
<html lang="en">
<head>
<meta charset="utf-8">
<title>Brightkey Property Management – Postcard</title>
<link href="https://fonts.googleapis.com/css2?family=Montserrat:wght@400;500;600;700;800&display=swap" rel="stylesheet">
<style>
:root{
  --brand-blue:#1c4a82;
  --brand-blue-dark:#153a68;
  --charcoal:#3b3b3d;
  --ink:#2b2b2b;
  --paper:#ffffff;
  --backdrop:#e4e3e5;
  --photo-light:#c9d6e0;
  --photo-dark:#5b6f86;
  --rule:#c8c8c8;
}
*{box-sizing:border-box;margin:0;padding:0}
html,body{width:1200px;height:867px;overflow:hidden}
body{background:var(--backdrop);font-family:"Montserrat",sans-serif;color:var(--ink);position:relative}
.postcard{position:absolute;top:243px;width:570px;height:380px;background:var(--paper);overflow:hidden;box-shadow:0 2px 6px rgba(0,0,0,.12)}
.postcard--back{left:20px}
.postcard--front{left:610px}

/* Back */
.offer-panel{position:absolute;left:0;top:0;width:330px;height:270px;background:var(--brand-blue);clip-path:polygon(0 0,100% 0,88% 100%,0 100%);padding:34px 40px 0 30px;color:var(--paper)}
.offer-title{font-size:21px;line-height:1.1;font-weight:500}
.offer-title strong{display:block;font-weight:800;font-size:25px}
.offer-list{list-style:none;margin-top:18px;font-size:12.5px;line-height:1.35;max-width:230px}
.offer-list li{margin-bottom:12px}
.call-block{position:absolute;left:30px;top:280px}
.call-label{font-size:17px;font-weight:700;color:var(--charcoal)}
.call-phone{display:inline-block;margin-top:4px;background:var(--brand-blue);color:var(--paper);font-weight:800;font-size:23px;padding:2px 22px;border-radius:20px;border:2px solid var(--brand-blue-dark)}
.call-web{font-size:12px;font-weight:700;color:var(--charcoal);margin-top:4px}
.back-footer{position:absolute;left:0;bottom:0;width:330px;height:18px;background:var(--charcoal)}
.mail-area{position:absolute;left:360px;top:150px;width:180px}
.mail-line{height:1px;background:var(--rule);margin-bottom:30px}

/* Front */
.photo{position:absolute;right:0;top:0;width:360px;height:248px;background:linear-gradient(135deg,var(--photo-light),var(--photo-dark))}
.hero-panel{position:absolute;left:0;top:0;width:240px;height:262px;background:var(--brand-blue);clip-path:polygon(0 0,92% 0,100% 100%,0 100%);padding:24px 20px 0 22px;color:var(--paper)}
.brand-name{font-size:15px;font-weight:700;letter-spacing:2px;line-height:1.2}
.headline{margin-top:26px;font-size:14px;font-weight:500;line-height:1.1}
.headline strong{display:block;font-weight:800;font-size:22px;line-height:1.05}
.headline-rule{width:56px;height:3px;background:var(--paper);margin:8px 0}
.tagline{font-size:10.5px;line-height:1.4}
.services{position:absolute;left:14px;top:268px;display:flex;gap:6px;list-style:none}
.service{width:62px;text-align:center;font-size:8.5px;font-weight:500;color:var(--charcoal);line-height:1.15}
.service svg{display:block;margin:0 auto 4px;width:32px;height:32px}
.front-footer{position:absolute;left:0;bottom:0;width:100%;height:46px;background:var(--charcoal);color:var(--paper);display:flex;align-items:center;justify-content:space-between;padding:0 18px;font-size:10.5px}
.front-footer .item{display:flex;align-items:center;gap:6px}
.front-footer .phone{font-size:15px;font-weight:700}
.front-footer .web{font-weight:700}
</style>
</head>
<body>

<section class="postcard postcard--back" aria-label="Postcard back">
  <div class="offer-panel">
    <h2 class="offer-title">GET A FREE <strong>RENTAL ANALYSIS</strong></h2>
    <ul class="offer-list">
      <li>Determine the rental value of your property.</li>
      <li>Find out how to get the most out of your investment.</li>
      <li>See if your home fits our management approach.</li>
    </ul>
  </div>
  <div class="call-block">
    <p class="call-label">GIVE US A CALL NOW</p>
    <p class="call-phone">555-014-2286</p>
    <p class="call-web">www.brightkeyrentals-example.com</p>
  </div>
  <div class="back-footer"></div>
  <div class="mail-area" aria-label="Recipient address">
    <div class="mail-line"></div>
    <div class="mail-line"></div>
    <div class="mail-line"></div>
  </div>
</section>

<section class="postcard postcard--front" aria-label="Postcard front">
  <div class="photo" role="img" aria-label="Photo of a property manager and a client reviewing a laptop in a bright office"></div>
  <div class="hero-panel">
    <p class="brand-name">BRIGHTKEY<br>PROPERTY MANAGEMENT</p>
    <h1 class="headline">CHOOSE THE RIGHT <strong>PROPERTY MANAGEMENT</strong> SYSTEM</h1>
    <div class="headline-rule"></div>
    <p class="tagline">Selecting the wrong manager could be your costliest mistake ever.</p>
  </div>

  <ul class="services">
    <li class="service"><svg viewBox="0 0 32 32"><circle cx="16" cy="16" r="15" fill="none" stroke="#1c4a82" stroke-width="1.5"/><path d="M8 16 16 9l8 7M11 14v8h10v-8" fill="none" stroke="#3b3b3d" stroke-width="2"/></svg>Property Marketing</li>
    <li class="service"><svg viewBox="0 0 32 32"><circle cx="16" cy="16" r="15" fill="none" stroke="#1c4a82" stroke-width="1.5"/><circle cx="16" cy="12" r="3" fill="#3b3b3d"/><circle cx="10" cy="14" r="2.3" fill="#3b3b3d"/><circle cx="22" cy="14" r="2.3" fill="#3b3b3d"/><path d="M10 22a6 5 0 0 1 12 0z M5 22a5 4 0 0 1 7-3 M27 22a5 4 0 0 0-7-3" fill="#3b3b3d"/></svg>Tenant Screening</li>
    <li class="service"><svg viewBox="0 0 32 32"><circle cx="16" cy="16" r="15" fill="none" stroke="#1c4a82" stroke-width="1.5"/><text x="16" y="22" text-anchor="middle" font-family="Montserrat,sans-serif" font-weight="700" font-size="16" fill="#3b3b3d">$</text></svg>Rent Collection</li>
    <li class="service"><svg viewBox="0 0 32 32"><circle cx="16" cy="16" r="15" fill="none" stroke="#1c4a82" stroke-width="1.5"/><path d="M11 10h9l2 3h-11z" fill="#3b3b3d"/><path d="M16 13l5 10" stroke="#3b3b3d" stroke-width="2.5"/></svg>Maintenance</li>
    <li class="service"><svg viewBox="0 0 32 32"><circle cx="16" cy="16" r="15" fill="none" stroke="#1c4a82" stroke-width="1.5"/><circle cx="17" cy="14" r="5" fill="none" stroke="#3b3b3d" stroke-width="2"/><path d="M13 18l-5 5" stroke="#3b3b3d" stroke-width="2.5"/></svg>Property Inspections</li>
    <li class="service"><svg viewBox="0 0 32 32"><circle cx="16" cy="16" r="15" fill="none" stroke="#1c4a82" stroke-width="1.5"/><rect x="9" y="9" width="14" height="14" fill="none" stroke="#3b3b3d" stroke-width="1.5"/><rect x="11" y="16" width="2.5" height="5" fill="#3b3b3d"/><rect x="15" y="13" width="2.5" height="8" fill="#3b3b3d"/><rect x="19" y="11" width="2.5" height="10" fill="#3b3b3d"/></svg>Financial Reporting</li>
    <li class="service"><svg viewBox="0 0 32 32"><circle cx="16" cy="16" r="15" fill="none" stroke="#1c4a82" stroke-width="1.5"/><path d="M16 8l7 3v5c0 4-3 7-7 8-4-1-7-4-7-8v-5z" fill="#3b3b3d"/></svg>Evictions</li>
    <li class="service"><svg viewBox="0 0 32 32"><circle cx="16" cy="16" r="15" fill="none" stroke="#1c4a82" stroke-width="1.5"/><path d="M16 8v15M11 23h10M9 11h14M9 11l-3 6h6zM23 11l-3 6h6z" fill="none" stroke="#3b3b3d" stroke-width="1.5"/></svg>Legal Guidance</li>
  </ul>

  <footer class="front-footer">
    <span class="item"><svg width="10" height="14" viewBox="0 0 10 14"><path d="M5 0a5 5 0 0 1 5 5c0 4-5 9-5 9S0 9 0 5a5 5 0 0 1 5-5z" fill="#fff"/><circle cx="5" cy="5" r="2" fill="#3b3b3d"/></svg>2287 Marble Lane<br>Lubbock, TX 79555</span>
    <span class="item phone"><svg width="13" height="13" viewBox="0 0 24 24"><path d="M6 2l4 4-2 3c1 3 4 6 7 7l3-2 4 4-3 4C10 22 2 14 2 5z" fill="#fff"/></svg>555-014-2286</span>
    <span class="item web">www.brightkeyrentals-example.com</span>
  </footer>
</section>

</body>
</html>
```